Create a Flyer for a Darts Tournament

We need a Flyer for a Darts Tournament that is going to be organized by our darts department (logo attached). The name of the tournament is "3. KLW Dartsturnier". The Flyer should look modern, professional and in a way that everyone can see at the first impression that is has to do with dart sports. The logo of our department should be on the flyer as well. On the flyer we need an area where we can place some informations regarding the tournament (bullet points) etc. And a area where we can place informations regarding the registration progress (e.g. "Registration via E-Mail". Should fit well to our logo.

Target Market(s)

Darts Players for the Tournament

Font styles to use
Serif

Colors

Designer to choose colors to be used in the design.

Requirements
Must have
• Name of the Tournament, our Logo, place for some tournament details, link to our registration page (besucher.tv-hallwitz.de). Should

```html
<!DOCTYPE html>
<html lang="de">
<head>
<meta charset="utf-8">
<title>3. KLW Dartsturnier</title>
<link href="https://fonts.googleapis.com/css2?family=Poppins:wght@400;500;600;800&display=swap" rel="stylesheet">
<style>
  :root {
    --navy-deep: #030d2e;
    --navy: #06205a;
    --blue-mid: #0d4fa8;
    --accent: #0aa8ec;
    --sky: #5cc7f0;
    --board-light: #dfe7ee;
    --board-dark: #12151c;
    --white: #ffffff;
  }
  * { margin: 0; padding: 0; box-sizing: border-box; }
  html, body { width: 848px; height: 1200px; overflow: hidden; background: var(--navy-deep); }
  body { font-family: 'Poppins', sans-serif; color: var(--white); }
  .flyer { position: relative; width: 848px; height: 1200px; overflow: hidden;
    background: linear-gradient(180deg, #04133d 0%, #062a6e 62%, #0a3f93 72%, #051a4c 86%, var(--navy-deep) 100%); }

  .hero-photo { position: absolute; left: 0; top: 0; width: 848px; height: 900px;
    background:
      radial-gradient(ellipse 150px 150px at 545px 370px, rgba(240,245,250,.55) 0%, rgba(240,245,250,0) 100%),
      radial-gradient(ellipse 330px 380px at 600px 380px, rgba(223,231,238,.55) 0%, rgba(60,130,200,.5) 45%, rgba(18,21,28,.55) 75%, rgba(18,21,28,0) 100%),
      radial-gradient(ellipse 200px 260px at 830px 480px, rgba(18,21,28,.8) 0%, rgba(18,21,28,0) 100%),
      radial-gradient(ellipse 240px 320px at 80px 500px, rgba(60,200,245,.75) 0%, rgba(15,90,170,.45) 50%, rgba(5,20,50,0) 100%),
      radial-gradient(ellipse 220px 160px at 300px 260px, rgba(40,140,230,.45) 0%, rgba(40,140,230,0) 100%),
      radial-gradient(ellipse 260px 200px at 700px 760px, rgba(90,190,240,.6) 0%, rgba(90,190,240,0) 100%),
      linear-gradient(150deg, #03112f 0%, #052259 35%, #0b3f8c 65%, #1c8fd6 88%, #0c4590 100%);
    -webkit-mask-image: linear-gradient(180deg, #000 0%, #000 70%, transparent 100%);
            mask-image: linear-gradient(180deg, #000 0%, #000 70%, transparent 100%); }

  .club-mark { position: absolute; left: 36px; top: 136px; display: flex; align-items: center; gap: 10px;
    font-weight: 800; font-size: 32px; color: var(--white); }
  .club-mark .dot { width: 24px; height: 24px; border-radius: 50%; background: var(--accent); }

  .title { position: absolute; left: 40px; top: 650px; line-height: 1; }
  .title-edition { font-weight: 800; font-size: 130px; letter-spacing: -2px; color: var(--white); }
  .title-name { font-weight: 800; font-size: 68px; color: var(--accent); margin-top: -8px; letter-spacing: -.5px; }

  .facts-heading { position: absolute; left: 42px; top: 862px; font-weight: 800; font-size: 56px; line-height: 1; }

  .facts-list { position: absolute; list-style: none; }
  .facts-list li { position: relative; padding-left: 28px; font-size: 17.5px; font-weight: 500; height: 37.5px; line-height: 22px; white-space: nowrap; }
  .facts-list li::before { content: ""; position: absolute; left: 0; top: 3px; width: 16px; height: 16px; border-radius: 4px; background: var(--accent); }
  .facts-left { left: 46px; top: 934px; }
  .facts-right { left: 524px; top: 936px; }

  .contact { position: absolute; line-height: 1.2; }
  .contact-label { color: var(--accent); font-weight: 600; font-size: 19px; }
  .contact-link { font-size: 19px; font-weight: 500; color: var(--white); }
  .registration { left: 43px; top: 1106px; }
  .registration::after { content: ""; display: block; width: 177px; height: 3px; background: var(--accent); margin-top: 3px; }
  .info { left: 605px; top: 1115px; }
</style>
</head>
<body>
<main class="flyer">
  <div class="hero-photo" role="img" aria-label="Photo of a blue dart hitting the bullseye of a blurred dartboard in front of a worn blue, white and black dartboard"></div>

  <div class="club-mark"><span class="dot"></span>KLW Darts</div>

  <h1 class="title">
    <div class="title-edition">03. KLW</div>
    <div class="title-name">DARTSTURNIER</div>
  </h1>

  <h2 class="facts-heading">FACTS</h2>
  <ul class="facts-list facts-left">
    <li>Samstag, 25.01.2025</li>
    <li>Einlass 16:00 Uhr / Turnierbeginn 17:00 Uhr</li>
    <li>Steel-Darts-Hobbyturnier (keine Ligaspieler)</li>
    <li>SVZ in 04567 Hallwitz-Nord</li>
  </ul>
  <ul class="facts-list facts-right">
    <li>Maximal 48 Teilnehmer</li>
    <li>Gruppenphase 301 | DO | BO3</li>
    <li>KO-Phase 501 | DO | BO5</li>
  </ul>

  <div class="contact registration">
    <div class="contact-label">Anmeldung:</div>
    <div class="contact-link">besucher.tv-hallwitz.de</div>
  </div>
  <div class="contact info">
    <div class="contact-label">Infos:</div>
    <div class="contact-link">darts.tv-hallwitz.de</div>
  </div>
</main>
</body>
</html>
```